Float and wellness centre needs a website refresh

Our float and wellness centre has been operating in Brisbane, Australia for 3 months. Our website is functional and easy to use, but it lacks a compelling visual experience that sells our awesome services to our customers.<br/><br/>We would like a complete redesign of our webpage. It is very important that the redesign considers the page layout for mobile users and the winning design will need to show both a desktop and mobile version of each of the pages listed below.<br/><br/>Out current website can be found at https://www.ebbtidehaven.com.au/<br/><br/>The winning design will need to provide proposals for redesigning the 4 pages listed below:<br/>Home Page - https://www.ebbtidehaven.com.au/<br/>Float Page - https://www.ebbtidehaven.com.au/services/float<br/>Build Gift Card page - https://www.ebbtidehaven.com.au/giftcard/stepone?location=kelsworth<br/>Booking Page - https://www.ebbtidehaven.com.au/Calendar/Day?centerId=kelsworth&selectedCategory=FLOAT&date=12/18/2019%2000:00:00%20+10:00&sessionLength=60<br/><br/>We only need the 4 pages listed above as our web developer will use the assets from the above pages to standardize all the other pages in the site. It is very important your proposed pages contain the same information as our current pages so that we can properly see the complete layout.<br/><br/>The Home page must display the business logo in some way. We would like the website to have a white background and for it make tasteful use of color to highlight key features on the pages. Where color is used it should harmonize with the business logo. The website needs to feel bright, simple and relaxing. Our current site does not use images very well and we have had professional photos taken of the center and the float rooms specifically for this website project. You can download these, and the business logo images here: http://ebbtidehaven.com.au/websiteimages.zip <br/><br/>We have included a few links below to other centers who have pages that we like: <br/><br/>https://www.drifthollowpods.com/ <br/>https://www.quietnook.com.au/ <br/>https://www.moonbaysoak.com.au/<br/>

Industry/Entity Type

Health And Wellness

Number of Pages Required

4 page

Font styles to use
Sans Serif

Colors

Designer to choose colors to be used in the design.

Requirements
Must have
• It is very important your proposed pages contain the same information as our current pages so that we can properly see the complete layout.
• The Home page must display the business logo in some way.
• Where color is used it should harmonize with the business logo.
Nice to have
• The website needs to feel bright, simple and relaxing. Our current site does not use images very well and we have had professional photos taken of the center and the float rooms specifically for this website project. You can download these, and the business logo images here: http://ebbtidehaven.com.au/websiteimages.zip
Should not have
• Dark pages.

```html
<!DOCTYPE html>
<html lang="en">
<head>
<meta charset="utf-8">
<title>Ebbtide Haven – Book</title>
<link href="https://fonts.googleapis.com/css2?family=Source+Sans+3:wght@400;600;700&display=swap" rel="stylesheet">
<style>
  :root{
    --mat:#fbf9fa;
    --page-bg:#d9d9d9;
    --plum:#9e5880;
    --plum-text:#a0567e;
    --card:#f4ecf1;
    --ink:#444049;
    --muted:#8a8590;
    --field-line:#b9b4bb;
    --field-grey:#e4e2e4;
    --white:#ffffff;
    --pink:#e0457f;
    --sky:#5a7fd0;
  }
  *{margin:0;padding:0;box-sizing:border-box}
  html,body{width:1200px;height:1200px;overflow:hidden;background:var(--mat);
    font-family:"Source Sans 3","Source Sans Pro",sans-serif;color:var(--ink)}
  .page{position:absolute;left:406px;top:177px;width:556px;height:1050px;
    transform:scale(.6211);transform-origin:0 0;background:var(--page-bg);overflow:hidden}
  .abs{position:absolute}
  .backdrop{position:absolute;inset:0}
  .nav{position:absolute;top:8px;left:0;width:556px;height:14px;font-size:8.5px;font-weight:600;color:#e6e0f0}
  .nav span{position:absolute;top:0;white-space:nowrap}
  .nav .current{color:var(--pink)}
  .nav .login{font-weight:700;color:var(--white);font-size:9px}
  .brand-mark{position:absolute;display:flex;align-items:center;gap:4px;font-weight:700;white-space:nowrap}
  .brand-mark i{display:block;border-radius:50%}
  .hero-title{position:absolute;left:163px;top:92px;line-height:1}
  .hero-title .kicker{display:block;font-size:25px;font-weight:600;color:var(--plum-text)}
  .hero-title .headline{display:block;font-size:27px;font-weight:700;color:var(--white);margin-top:9px}
  .card{position:absolute;left:51px;top:344px;width:461px;height:451px;background:var(--card);border-radius:8px}
  .ribbon-label{position:absolute;left:305px;top:419px;transform:translate(-50%,-50%) rotate(8deg);
    font-size:18px;font-weight:700;color:var(--white);letter-spacing:.5px}
  .spa-name{position:absolute;left:186px;top:504px;font-size:7px;font-weight:700}
  .form-title{position:absolute;left:0;width:556px;top:577px;text-align:center;font-size:7px;font-weight:700}
  .label{position:absolute;right:397px;font-size:6.8px;font-weight:700;text-align:right;white-space:nowrap}
  .field{position:absolute;height:14px;border:1px solid var(--field-line);border-radius:4px;background:var(--white);
    font-size:6.5px;color:var(--muted);padding-left:5px;line-height:12px}
  .field .arrows{position:absolute;right:3px;top:1px;font-size:5px;line-height:5px;color:var(--ink)}
  .field.grey{background:var(--field-grey);color:var(--ink);font-weight:600}
  .to{position:absolute;left:312px;top:628px;font-size:7px}
  .cta{position:absolute;left:197px;top:726px;width:167px;height:26px;background:var(--plum);border-radius:3px;
    color:var(--white);font-size:9.5px;font-weight:700;text-align:center;line-height:26px}
  .foot-links{position:absolute;font-size:7px;line-height:10.4px;color:var(--white);text-align:center}
  .social{position:absolute;left:483px;top:1009px;color:var(--white);font-size:7px;font-weight:700}
  .social-box{position:absolute;top:1022px;width:14px;height:14px;border:1.5px solid var(--white);border-radius:3px}
</style>
</head>
<body>
<main class="page">
  <svg class="backdrop" width="556" height="1050" viewBox="0 0 556 1050">
    <defs>
      <linearGradient id="heroTone" x1="0" y1="0" x2="1" y2="0.4">
        <stop offset="0" stop-color="#3d4cc0"/>
        <stop offset=".45" stop-color="#4f3fa6"/>
        <stop offset="1" stop-color="#4a2c44"/>
      </linearGradient>
      <radialGradient id="softGlow" cx=".5" cy=".4" r=".6">
        <stop offset="0" stop-color="#c6cfd6"/>
        <stop offset="1" stop-color="#cdd6d8" stop-opacity="0"/>
      </radialGradient>
    </defs>
    <rect class="decor-upper" x="90" y="200" width="380" height="150" fill="url(#softGlow)" role="img" aria-label="Faint decorative wellness motif"/>
    <rect class="decor-lower" x="95" y="790" width="375" height="140" fill="url(#softGlow)" role="img" aria-label="Faint decorative wellness motif"/>
    <polygon class="hero-photo" points="0,0 556,0 556,178 285,248 0,174" fill="url(#heroTone)" role="img" aria-label="Photo of a guest floating in a lit float pool"/>
    <polygon points="24,360 51,356 51,365" fill="var(--sky)"/>
    <polygon points="537,472 513,476 513,468" fill="var(--sky)"/>
    <polygon class="footer-band" points="0,968 278,917 556,968 556,1050 0,1050" fill="var(--plum)"/>
  </svg>

  <div class="brand-mark" style="left:14px;top:40px;font-size:9px;color:var(--white)"><i style="width:10px;height:10px;background:var(--pink)"></i>Ebbtide Haven</div>

  <nav class="nav">
    <span style="left:201px">Home</span>
    <span class="current" style="left:248px">Float</span>
    <span style="left:293px">IR Sauna</span>
    <span style="left:352px">mHBOT</span>
    <span style="left:405px">Heat Mat</span>
    <span style="left:460px">Gift cards</span>
    <span class="login" style="left:521px;top:-1px">Login</span>
  </nav>

  <h1 class="hero-title"><span class="kicker">EBBTIDE</span><span class="headline">BOOK.</span></h1>

  <section class="card"></section>
  <svg class="abs" style="left:0;top:0" width="556" height="500" viewBox="0 0 556 500">
    <polygon points="24,360 537,432 537,472 24,398" fill="var(--plum)"/>
  </svg>
  <div class="ribbon-label">BOOK</div>

  <div class="spa-name">Ebbtide Haven</div>
  <div class="brand-mark" style="left:352px;top:508px;font-size:9px;color:var(--plum-text)"><i style="width:10px;height:10px;background:var(--plum-text)"></i>Ebbtide Haven</div>

  <div class="form-title">Book a New Appoinment</div>

  <div class="label" style="top:602px">Filter By Date</div>
  <div class="field" style="left:169px;top:599px;width:294px">Wednesday,20th November 2019<span class="arrows">▲<br>▼</span></div>

  <div class="label" style="top:628px">Filter By Time</div>
  <div class="field" style="left:169px;top:625px;width:124px">All Day<span class="arrows">▲<br>▼</span></div>
  <div class="to">to</div>
  <div class="field grey" style="left:339px;top:625px;width:124px">Select a Time<span class="arrows">▲<br>▼</span></div>

  <div class="label" style="top:653px">Filter By Categorie</div>
  <div class="field" style="left:169px;top:650px;width:294px">Any Categorie<span class="arrows">▲<br>▼</span></div>

  <div class="label" style="top:680px">Filter By Service</div>
  <div class="field" style="left:169px;top:678px;width:294px">Any Service<span class="arrows">▲<br>▼</span></div>

  <div class="cta">Show all availability</div>

  <div class="brand-mark" style="left:244px;top:958px;font-size:10px;color:var(--white)"><i style="width:9px;height:9px;background:var(--white)"></i>Ebbtide Haven</div>

  <div class="foot-links" style="left:24px;top:998px;width:100px">Booking Policy<br>Membership Policy<br>Privacy Policy<br>Cancellation Policy</div>
  <div class="foot-links" style="left:238px;top:1013px;width:80px">FAQs<br>Sitemap</div>
  <div class="social">Follow US</div>
  <div class="social-box" style="left:482px" aria-label="Social profile"></div>
  <div class="social-box" style="left:505px" aria-label="Social profile"></div>
</main>
</body>
</html>
```